KORBALT

The business want a professional looking business card. We have a scetch we will add but want the extra upgrade, and would like more suggestions for variations of our business cards.

```html
<!DOCTYPE html>
<html lang="en">
<head>
<meta charset="utf-8">
<title>KORBALT Business Cards</title>
<link href="https://fonts.googleapis.com/css2?family=Poppins:wght@400;500&display=swap" rel="stylesheet">
<style>
  :root {
    --backdrop: #3b3b3b;
    --card: #262626;
    --gold: #d8b340;
    --gold-soft: #b8963a;
  }
  * { margin: 0; padding: 0; box-sizing: border-box; }
  html, body {
    width: 1200px; height: 800px; overflow: hidden;
    background: var(--backdrop);
    font-family: "Poppins", sans-serif;
  }
  .canvas { position: relative; width: 1200px; height: 800px; }
  .card {
    position: absolute;
    width: 525px; height: 300px;
    background: var(--card);
    color: var(--gold);
  }
  .card--front { left: 140px; top: 70px; }
  .card--back  { left: 535px; top: 430px; }

  /* Front */
  .front-brand {
    position: absolute; inset: 0;
    display: flex; flex-direction: column; align-items: center; justify-content: center;
  }
  .brand-dot {
    width: 22px; height: 22px; border-radius: 50%;
    background: var(--gold); margin-bottom: 26px;
  }
  .brand-name {
    font-weight: 500; font-size: 38px; letter-spacing: 10px;
    padding-left: 10px; line-height: 1;
  }
  .brand-tagline {
    margin-top: 14px; font-size: 13px; letter-spacing: 9px; padding-left: 9px;
  }

  /* Back */
  .back-brand {
    position: absolute; left: 0; top: 0; width: 180px; height: 100%;
    display: flex; flex-direction: column; align-items: center; justify-content: center;
  }
  .back-brand .brand-dot { width: 16px; height: 16px; margin-bottom: 14px; }
  .back-brand .brand-name { font-size: 20px; letter-spacing: 4px; padding-left: 4px; }
  .divider {
    position: absolute; left: 180px; top: 40px; width: 1px; height: 220px;
    background: var(--gold-soft);
  }
  .contact-block { position: absolute; left: 210px; top: 40px; right: 20px; height: 220px; }
  .person-name { font-size: 21px; font-weight: 500; line-height: 1.2; }
  .person-role { font-size: 14px; margin-top: 4px; }
  .contact-list {
    position: absolute; left: 0; bottom: 0; list-style: none;
    font-size: 14px; line-height: 1;
  }
  .contact-list li { display: flex; align-items: center; gap: 12px; margin-top: 8px; }
  .contact-list svg { width: 15px; height: 15px; flex: none; }
</style>
</head>
<body>
<main class="canvas">
  <section class="card card--front">
    <div class="front-brand">
      <span class="brand-dot"></span>
      <div class="brand-name">KORBALT</div>
      <div class="brand-tagline">APPAREL</div>
    </div>
  </section>

  <section class="card card--back">
    <div class="back-brand">
      <span class="brand-dot"></span>
      <div class="brand-name">KORBALT</div>
    </div>
    <div class="divider"></div>
    <div class="contact-block">
      <h1 class="person-name">Anders Holm Vikersund</h1>
      <p class="person-role">CEO &amp; Founder</p>
      <ul class="contact-list">
        <li>
          <svg viewBox="0 0 16 16" fill="none" stroke="currentColor" stroke-width="1.4"><rect x="4" y="1.5" width="8" height="13" rx="1.5"/><line x1="7" y1="12" x2="9" y2="12"/></svg>
          <span>004790415527</span>
        </li>
        <li>
          <svg viewBox="0 0 16 16" fill="none" stroke="currentColor" stroke-width="1.4"><rect x="1.5" y="3.5" width="13" height="9" rx="1"/><path d="M1.8 4l6.2 5 6.2-5"/></svg>
          <span>korbalt.llc@postmail.com</span>
        </li>
        <li>
          <svg viewBox="0 0 16 16" fill="none" stroke="currentColor" stroke-width="1.4"><circle cx="8" cy="8" r="6.5"/><ellipse cx="8" cy="8" rx="2.8" ry="6.5"/><line x1="1.5" y1="8" x2="14.5" y2="8"/></svg>
          <span>www.korbalt.llc</span>
        </li>
      </ul>
    </div>
  </section>
</main>
</body>
</html>
```